Townhome Multi-Family Property Exterior Sign

Hello. We are looking for a new design for our exterior pylon for for a multi-family housing property in Texas. The design will need to go on a new sign panel to replace the existing (see photo of existing). We are looking to see both modern and contemporary designs. Included the sign should be the name, Loma Brisa Townhomes and the web address www.lomabrisatownhomes.example.

Attached here is a PDF file of the proposed new sign shape. We are open to other shape ideas as well if your design would better suit a more rectangular shape.

Industry/Entity Type

Property

Font styles to use
Serif
Sans Serif

Colors
9bcb3c

Requirements
Must have
• Name of building: Loma Brisa Townhomes
• Website: www.lomabrisatownhomes.example
Nice to have
• Address: 412-590 Halvern Ridge Drive (only if it fits nicely)

```html
<!DOCTYPE html>
<html lang="en">
<head>
<meta charset="utf-8">
<title>Loma Brisa Townhomes — Sign Panel Concepts</title>
<link rel="stylesheet" href="https://fonts.googleapis.com/css2?family=Libre+Baskerville:wght@700&family=Montserrat:wght@700;800&display=swap">
<style>
  :root {
    --page-bg: #ffffff;
    --panel-green: #0f763f;
    --accent-white: #ffffff;
    --accent-lime: #9bcb3c;
  }
  html, body {
    margin: 0;
    padding: 0;
    width: 1200px;
    height: 1001px;
    overflow: hidden;
    background: var(--page-bg);
  }
  .canvas {
    position: relative;
    width: 1200px;
    height: 1001px;
  }
  .sign-panel {
    position: absolute;
    display: block;
  }
  .sign-panel--classic { left: 88px; top: 148px; width: 414px; height: 207px; }
  .sign-panel--lime { left: 688px; top: 646px; width: 418px; height: 209px; }

  .panel-body { fill: var(--panel-green); }
  .panel-frame { fill: none; stroke-width: 5; }
  .sign-panel--classic .panel-frame { stroke: var(--accent-white); }
  .sign-panel--lime .panel-frame { stroke: var(--accent-lime); stroke-width: 6; }
  .sign-panel--classic .tagline-band { fill: var(--accent-white); }
  .sign-panel--lime .tagline-band { fill: var(--accent-lime); }

  .property-name {
    font-family: "Libre Baskerville", Georgia, serif;
    font-weight: 700;
    font-size: 58px;
    fill: var(--accent-white);
  }
  .property-tagline {
    font-family: "Montserrat", Arial, sans-serif;
    font-weight: 800;
    font-size: 19px;
    letter-spacing: 15px;
  }
  .sign-panel--classic .property-tagline { fill: var(--panel-green); }
  .sign-panel--lime .property-tagline { fill: var(--accent-white); }
  .property-web {
    font-family: "Montserrat", Arial, sans-serif;
    font-weight: 700;
    font-size: 14px;
    letter-spacing: 0.6px;
    fill: var(--accent-white);
  }
</style>
</head>
<body>
<main class="canvas">

  <svg class="sign-panel sign-panel--classic" viewBox="0 0 510 255" aria-label="Loma Brisa Townhomes sign, green and white">
    <path class="panel-body" d="M0,68 Q70,62 130,34 Q255,-18 380,34 Q440,60 510,62 L510,255 L0,255 Z"/>
    <path class="panel-frame" d="M12,80 Q76,74 134,48 Q255,-2 376,48 Q436,72 498,74 L498,243 L12,243 Z"/>
    <rect class="tagline-band" x="12" y="160" width="486" height="28"/>
    <text class="property-name" x="255" y="145" text-anchor="middle">Loma Brisa</text>
    <text class="property-tagline" x="262" y="181" text-anchor="middle">TOWNHOMES</text>
    <text class="property-web" x="255" y="222" text-anchor="middle">WWW.LOMABRISATOWNHOMES.EXAMPLE</text>
  </svg>

  <svg class="sign-panel sign-panel--lime" viewBox="0 0 510 255" aria-label="Loma Brisa Townhomes sign, green and lime">
    <path class="panel-body" d="M0,68 Q70,62 130,34 Q255,-18 380,34 Q440,60 510,62 L510,255 L0,255 Z"/>
    <path class="panel-frame" d="M12,80 Q76,74 134,48 Q255,-2 376,48 Q436,72 498,74 L498,243 L12,243 Z"/>
    <rect class="tagline-band" x="12" y="160" width="486" height="28"/>
    <text class="property-name" x="255" y="145" text-anchor="middle">Loma Brisa</text>
    <text class="property-tagline" x="262" y="181" text-anchor="middle">TOWNHOMES</text>
    <text class="property-web" x="255" y="222" text-anchor="middle">WWW.LOMABRISATOWNHOMES.EXAMPLE</text>
  </svg>

</main>
</body>
</html>
```